Pellor Digital needs graphic icons for its products

Mintra Loom has designed our logo, and now we would like to create product labels for our products. We think of them like buttons, to use on the site, on presentations, so that we may fast recognize the products. They are:
E-Learning Suite; Digital Signage; Corporate TV; Content Media Encoder; Webcast; E-Commerce Suite; Online Video Platform.
See the company's logo attached.
Updates
Reason: I have to extend for more 5 days, mainly because of the few ideas I have received.
Thanks,
Industry/Entity Type
Digital
Look and feel
Each slider illustrates characteristics of the customer's brand and the style your logo design should communicate.

```html
<!DOCTYPE html>
<html lang="en">
<head>
<meta charset="utf-8">
<title>Pellor Digital – Product Labels</title>
<link href="https://fonts.googleapis.com/css2?family=Open+Sans:wght@400&display=swap" rel="stylesheet">
<style>
  :root {
    --brand-red: #9b2622;
    --slate: #55585a;
    --icon-ink: #4b4b4d;
    --disc: #ffffff;
    --label-text: #ffffff;
    --bg-center: #f6f6f6;
    --bg-edge: #dedede;
  }
  * { box-sizing: border-box; margin: 0; padding: 0; }
  html, body { width: 1180px; height: 1200px; overflow: hidden; }
  body {
    background: radial-gradient(ellipse at center, var(--bg-center) 45%, var(--bg-edge) 100%);
    font-family: "Open Sans", Arial, sans-serif;
  }
  .product-list {
    position: absolute;
    left: 173px;
    top: 88px;
    width: 834px;
    display: flex;
    flex-direction: column;
    gap: 15.5px;
    list-style: none;
  }
  .product-label {
    height: 133px;
    background: var(--brand-red);
    display: flex;
    align-items: center;
    position: relative;
  }
  .product-label--featured { background: var(--slate); }
  .product-icon {
    position: absolute;
    left: 48px;
    top: 10.5px;
    width: 112px;
    height: 112px;
  }
  .product-name {
    position: absolute;
    left: 223px;
    color: var(--label-text);
    font-size: 52px;
    font-weight: 400;
    letter-spacing: 0.2px;
    line-height: 1;
    white-space: nowrap;
  }
  .ink { fill: var(--icon-ink); }
  .ink-line { stroke: var(--icon-ink); fill: none; }
  .red { fill: var(--brand-red); }
  .red-line { stroke: var(--brand-red); fill: none; }
  .disc { fill: var(--disc); }
</style>
</head>
<body>
<ul class="product-list">
  <li class="product-label">
    <svg class="product-icon" viewBox="0 0 112 112" aria-hidden="true">
      <circle class="disc" cx="56" cy="56" r="56"/>
      <rect class="ink" x="27" y="30" width="58" height="42" rx="3"/>
      <rect class="disc" x="31" y="34" width="50" height="32"/>
      <path class="ink" d="M37 39 q9 -3 18 2 v22 q-9 -4 -18 -1 z M57 41 q9 -5 18 -2 v23 q-9 -3 -18 1 z"/>
      <path class="disc" d="M40 44 h12 M40 48 h12 M40 52 h12 M40 56 h12 M60 44 h12 M60 48 h12 M60 52 h12 M60 56 h12" stroke="#fff" stroke-width="1.5"/>
      <rect class="ink" x="50" y="72" width="12" height="7"/>
      <rect class="ink" x="41" y="79" width="30" height="4" rx="1"/>
    </svg>
    <span class="product-name">E-Learning Suite</span>
  </li>
  <li class="product-label">
    <svg class="product-icon" viewBox="0 0 112 112" aria-hidden="true">
      <circle class="disc" cx="56" cy="56" r="56"/>
      <rect class="ink" x="29" y="25" width="54" height="50" rx="5"/>
      <rect class="disc" x="33" y="29" width="46" height="42" rx="2"/>
      <rect class="ink-line" x="37" y="33" width="38" height="34" stroke-width="2"/>
      <rect class="ink" x="52" y="75" width="8" height="10"/>
      <rect class="ink" x="41" y="85" width="30" height="4" rx="1"/>
    </svg>
    <span class="product-name">Digital Signage</span>
  </li>
  <li class="product-label product-label--featured">
    <svg class="product-icon" viewBox="0 0 112 112" aria-hidden="true">
      <circle class="disc" cx="56" cy="56" r="56"/>
      <path class="red-line" d="M56 36 L46 27 M56 36 L68 23" stroke-width="3" stroke-linecap="round"/>
      <rect class="red" x="26" y="36" width="60" height="40" rx="3"/>
      <rect class="disc" x="31" y="41" width="42" height="30"/>
      <circle class="disc" cx="79.5" cy="46" r="2.2"/>
      <circle class="disc" cx="79.5" cy="53" r="2.2"/>
      <rect class="red" x="48" y="76" width="16" height="5"/>
      <rect class="red" x="40" y="81" width="32" height="3" rx="1"/>
    </svg>
    <span class="product-name">Corporate TV</span>
  </li>
  <li class="product-label">
    <svg class="product-icon" viewBox="0 0 112 112" aria-hidden="true">
      <circle class="disc" cx="56" cy="56" r="56"/>
      <rect class="ink" x="34" y="25" width="44" height="62" rx="2"/>
      <g class="disc">
        <rect x="37" y="29" width="5" height="6"/><rect x="37" y="39" width="5" height="6"/>
        <rect x="37" y="49" width="5" height="6"/><rect x="37" y="59" width="5" height="6"/>
        <rect x="37" y="69" width="5" height="6"/><rect x="37" y="78" width="5" height="6"/>
        <rect x="70" y="29" width="5" height="6"/><rect x="70" y="39" width="5" height="6"/>
        <rect x="70" y="49" width="5" height="6"/><rect x="70" y="59" width="5" height="6"/>
        <rect x="70" y="69" width="5" height="6"/><rect x="70" y="78" width="5" height="6"/>
        <rect x="46" y="29" width="20" height="25"/>
        <rect x="46" y="58" width="20" height="26"/>
      </g>
    </svg>
    <span class="product-name">Content Media Encoder</span>
  </li>
  <li class="product-label">
    <svg class="product-icon" viewBox="0 0 112 112" aria-hidden="true">
      <circle class="disc" cx="56" cy="56" r="56"/>
      <circle class="ink" cx="56" cy="42" r="5"/>
      <path class="ink-line" d="M56 46 L44 86 M56 46 L68 86 M49 68 H63" stroke-width="4" stroke-linecap="round"/>
      <path class="ink-line" d="M46 32 a14 14 0 0 0 0 20 M66 32 a14 14 0 0 1 0 20 M39 26 a23 23 0 0 0 0 32 M73 26 a23 23 0 0 1 0 32" stroke-width="3.5" stroke-linecap="round"/>
    </svg>
    <span class="product-name">Webcast</span>
  </li>
  <li class="product-label">
    <svg class="product-icon" viewBox="0 0 112 112" aria-hidden="true">
      <circle class="disc" cx="56" cy="56" r="56"/>
      <path class="ink-line" d="M24 33 H33 L42 70 H80" stroke-width="4" stroke-linejoin="round" stroke-linecap="round"/>
      <path class="ink" d="M35 40 H86 L80 64 H41 z"/>
      <path d="M48 42 V62 M57 42 V62 M66 42 V62 M75 42 V62 M38 52 H83" stroke="#fff" stroke-width="2"/>
      <circle class="ink" cx="46" cy="80" r="5"/>
      <circle class="ink" cx="76" cy="80" r="5"/>
    </svg>
    <span class="product-name">E-Commerce Suite</span>
  </li>
  <li class="product-label">
    <svg class="product-icon" viewBox="0 0 112 112" aria-hidden="true">
      <circle class="disc" cx="56" cy="56" r="56"/>
      <rect class="ink-line" x="28" y="32" width="56" height="46" rx="2" stroke-width="3"/>
      <path class="ink" d="M50 44 L64 53 L50 62 z"/>
      <path class="ink-line" d="M34 70 H78" stroke-width="2"/>
      <circle class="ink" cx="46" cy="70" r="2.5"/>
    </svg>
    <span class="product-name">Online Video Platform</span>
  </li>
</ul>
</body>
</html>
```